Letterhead design for business

Looking for an attractive and professional letterhead that uses the logo that is attached below.

Target Market(s)

Potential bankruptcy clients.

Industry/Entity Type

Legal

Colors

Designer to choose colors to be used in the design.

Requirements
Must have
• Address for locations, phone number, and website address.
• Addresses are on website ferncoveadvice.example. Use following phone number (for tracking purposes): 555-013-8274

```html
<!DOCTYPE html>
<html lang="en">
<head>
<meta charset="utf-8">
<title>Ferncove Law Group — Letterhead</title>
<link href="https://fonts.googleapis.com/css2?family=Lato:wght@400;700&family=Pinyon+Script&display=swap" rel="stylesheet">
<style>
  :root {
    --green: #93c897;
    --ink: #1a1a1a;
    --charcoal: #4a4a4a;
    --rule: #e6e6e6;
    --paper: #ffffff;
  }
  * { margin: 0; padding: 0; box-sizing: border-box; }
  html, body { width: 848px; height: 1200px; overflow: hidden; background: var(--paper); }
  body { font-family: "Lato", sans-serif; color: var(--ink); }
  .letterhead { position: relative; width: 848px; height: 1200px; }

  .brand { position: absolute; left: 102px; top: 84px; display: flex; align-items: center; gap: 14px; }
  .brand-dot { width: 40px; height: 40px; border-radius: 50%; background: var(--green); }
  .brand-name { font-size: 30px; font-weight: 700; color: var(--charcoal); line-height: 1; }
  .brand-band { position: absolute; left: 428px; top: 92px; }

  .recipient { position: absolute; left: 102px; top: 190px; }
  .label-to { font-size: 20px; font-weight: 700; color: var(--green); margin-bottom: 13px; }
  .name { font-size: 20px; font-weight: 700; line-height: 1.2; }
  .name .accent { color: var(--green); }
  .detail { font-size: 16px; line-height: 21px; }
  .company { font-size: 20px; font-weight: 700; margin-top: 13px; line-height: 1.2; }

  .date { position: absolute; right: 79px; top: 331px; font-size: 17px; }
  .date strong { font-weight: 700; }

  .body { position: absolute; left: 102px; top: 418px; width: 670px; font-size: 16.6px; line-height: 20.5px; text-align: justify; }
  .body p + p { margin-top: 21px; }

  .signature { position: absolute; left: 102px; top: 912px; }
  .sign-script { font-family: "Pinyon Script", cursive; font-size: 40px; line-height: 1; }
  .sign-dots { font-size: 16px; letter-spacing: 2.6px; margin-top: 10px; line-height: 1; }
  .sign-name { font-size: 20px; font-weight: 700; letter-spacing: 2.8px; margin-top: 6px; }
  .sign-role { font-size: 16px; font-weight: 700; letter-spacing: 2px; }

  .footer-rule { position: absolute; left: 102px; top: 1064px; width: 668px; height: 4px; background: var(--rule); }
  .footer-rule::before, .footer-rule::after { content: ""; position: absolute; top: 0; height: 4px; width: 124px; background: var(--green); }
  .footer-rule::before { left: 0; }
  .footer-rule::after { right: 0; }

  .contact { position: absolute; top: 1088px; font-size: 16px; line-height: 21px; white-space: nowrap; }
  .contact svg { display: block; margin-bottom: 12px; }
  .contact-phone { left: 102px; }
  .contact-phone svg { margin-left: 46px; }
  .contact-web { left: 300px; width: 178px; text-align: center; }
  .contact-web svg { margin: 0 auto 14px; }
  .contact-address { left: 482px; }
  .contact-address svg { margin-left: 154px; }
</style>
</head>
<body>
<main class="letterhead">
  <div class="brand">
    <span class="brand-dot"></span>
    <span class="brand-name">Ferncove Law Group</span>
  </div>
  <svg class="brand-band" width="420" height="42" viewBox="0 0 420 42" aria-hidden="true">
    <polygon points="14,0 26,0 12,42 0,42" fill="var(--green)"/>
    <polygon points="32,0 44,0 30,42 18,42" fill="var(--green)"/>
    <polygon points="50,0 420,0 420,42 36,42" fill="var(--green)"/>
  </svg>

  <section class="recipient">
    <div class="label-to">TO</div>
    <div class="name">JOHN <span class="accent">DOE</span></div>
    <div class="detail">Manager</div>
    <div class="company">TECH GROUP</div>
    <div class="detail">77 Sevebth Avenue,<br>New York, USA.</div>
  </section>

  <div class="date"><strong>Date:</strong> 03-03-2018</div>

  <article class="body">
    <p>There are many variations of passages of Lorem Ipsum available, but the majority have suffered alteration in some form, by injected humour, or randomised words which don't look even slightly believable.</p>
    <p>If you are going to use a passage of Lorem Ipsum, you need to be sure there isn't anything embarrassing hidden in the middle of text. All the Lorem Ipsum generators on the Internet tend to repeat predefined chunks as necessary, making this the first true generator on the Internet.There are many variations of passages of Lorem Ipsum available, but the majority have suffered alteration in some form, by injected humour, or randomised words which don't look even slightly believable.</p>
    <p>If you are going to use a passage of Lorem Ipsum, you need to be sure there isn't anything embarrassing hidden in the middle of text. All the Lorem Ipsum generators on the Internet tend to repeat predefined chunks as necessary, making this the first true generator on the Internet.There are many variations of passages of Lorem Ipsum available, but the majority have suffered alteration in some form, by injected humour, or randomised words which don't look even slightly believable. If you are going to use a passage of Lorem Ipsum, you need to be sure there isn't anything embarrassing hidden in the middle of text.</p>
    <p>All the Lorem Ipsum generators on the Internet tend to repeat predefined chunks as necessary, making this the first true generator on the Internet.</p>
  </article>

  <section class="signature">
    <div class="sign-script">Jonathan Smith</div>
    <div class="sign-dots">.........................</div>
    <div class="sign-name">Jonathan Smith</div>
    <div class="sign-role">Director</div>
  </section>

  <div class="footer-rule"></div>

  <div class="contact contact-phone">
    <svg width="22" height="22" viewBox="0 0 24 24" aria-hidden="true"><path fill="var(--green)" d="M6.6 10.8a15.1 15.1 0 0 0 6.6 6.6l2.2-2.2a1 1 0 0 1 1-.25 11.4 11.4 0 0 0 3.6.57 1 1 0 0 1 1 1V20a1 1 0 0 1-1 1A17 17 0 0 1 3 4a1 1 0 0 1 1-1h3.5a1 1 0 0 1 1 1c0 1.250.2 2.46.57 3.6a1 1 0 0 1-.25 1z"/></svg>
    555-013-8274
  </div>
  <div class="contact contact-web">
    <svg width="24" height="24" viewBox="0 0 24 24" aria-hidden="true" fill="none" stroke="var(--green)" stroke-width="2"><circle cx="12" cy="12" r="10"/><path d="M2 12h20M12 2c3 3 3 17 0 20M12 2c-3 3-3 17 0 20M4 7h16M4 17h16"/></svg>
    ferncoveadvice.example
  </div>
  <div class="contact contact-address">
    <svg width="18" height="24" viewBox="0 0 18 24" aria-hidden="true"><path fill="var(--green)" d="M9 0a9 9 0 0 0-9 9c0 6.5 9 15 9 15s9-8.5 9-15a9 9 0 0 0-9-9zm0 12.5A3.5 3.5 0 1 1 9 5.5a3.5 3.5 0 0 1 0 7z"/></svg>
    418 Larkspur Rd., Suite #310 Brookhaven,<br>Georgia 30399
  </div>
</main>
</body>
</html>
```